Flyer Design Project

We are a coaching organisation that is about to launch classes catering to local and international university students in Australia. We would like a flyer that is fresh, captivating and ultimately pushes people to our website.
To understand the artistic approach to our business, visit our website: www.brightlanetutors.com.au
Updates
Hi designers, we have changed the criteria slightly to give you more creative license... Feel free to ask any questions, all the best.
Target Market(s)
International University Students aged between 18-25
Industry/Entity Type
University
Requirements
Must have
- Size: 1 sided A5 flyer
Must have logo on page
Introductory offer of 20% off all courses
Bright Lane Tutors exists to help university students with real life skill development such as public speaking. We aim to equip students with skills that are not taught in the university environment to enable them to maximise their results.
To find out more visit: www.brightlanetutors.com.au
CONTACT DETAILS: Leave space for 10 digit phone number
Nice to have
- Bold, eye catching design
Fresh, fun and professional look
Good use of typography
Should not have
- Do not use colours outside or that do not compliment our colour palette. You can view our three main colours (blue, pink, yellow) on our website.
www.brightlanetutors.com.au/courses/publicspeaking

```html
<!DOCTYPE html>
<html lang="en">
<head>
<meta charset="utf-8">
<title>Bright Lane Tutors – Flyer</title>
<link rel="stylesheet" href="https://fonts.googleapis.com/css2?family=Comic+Neue:wght@400;700&family=Noto+Sans+SC:wght@400;500&family=PT+Sans:wght@400&family=PT+Sans+Narrow:wght@700&display=swap">
<style>
  :root {
    --white: #ffffff;
    --sky: #5bb8ee;
    --rose: #f74f78;
    --sun: #fde54f;
    --navy: #1c3f8f;
    --cyan: #29b7e6;
    --ink: #111111;
    --hanzi: #f0457a;
  }
  html, body {
    margin: 0;
    padding: 0;
    width: 885px;
    height: 1200px;
    overflow: hidden;
    background: var(--white);
  }
  .flyer {
    position: relative;
    width: 885px;
    height: 1200px;
    overflow: hidden;
    background: var(--white);
  }
  .backdrop {
    position: absolute;
    inset: 0;
  }
  .brand-plate {
    position: absolute;
    left: 0;
    top: 92px;
    width: 500px;
    height: 186px;
    background: var(--white);
    border-radius: 0 16px 16px 0;
    box-shadow: 4px 6px 0 #cfcfd1;
    display: flex;
    align-items: center;
    gap: 22px;
    padding-left: 36px;
    box-sizing: border-box;
  }
  .brand-dot {
    width: 70px;
    height: 70px;
    border-radius: 50%;
    background: var(--cyan);
    flex: none;
  }
  .brand-name {
    font-family: "PT Sans", sans-serif;
    font-weight: 400;
    font-size: 54px;
    line-height: 1.0;
    color: var(--navy);
  }
  .offer {
    position: absolute;
    left: 550px;
    top: 220px;
    width: 300px;
    text-align: center;
    font-family: "PT Sans Narrow", sans-serif;
    font-weight: 700;
    color: var(--white);
    line-height: 1.3;
  }
  .offer-title { font-size: 40px; margin: 0; }
  .offer-detail { font-size: 32px; margin: 6px 0 0; }
  .checklist {
    position: absolute;
    left: 0;
    top: 0;
    width: 885px;
    height: 900px;
    margin: 0;
    padding: 0;
    list-style: none;
    font-family: "Comic Neue", cursive;
    font-weight: 700;
    font-size: 38px;
    color: var(--ink);
  }
  .checklist li {
    position: absolute;
    left: 54px;
    height: 60px;
    line-height: 60px;
    white-space: nowrap;
  }
  .checklist .zh {
    font-family: "Noto Sans SC", sans-serif;
    font-weight: 400;
    font-size: 56px;
    color: var(--hanzi);
    margin-left: 6px;
  }
  .item-subject { top: 483px; color: var(--navy); }
  .item-timetable { top: 550px; }
  .item-speaking { top: 617px; }
  .item-speaking-zh { top: 673px; left: 162px !important; }
  .item-speaking-zh .zh { margin-left: 0; }
  .item-fridge { top: 754px; }
  .item-best { top: 814px; }
  .web-link {
    position: absolute;
    left: 54px;
    top: 906px;
    font-family: "PT Sans", sans-serif;
    font-size: 27px;
    color: var(--cyan);
    margin: 0;
  }
  .about {
    position: absolute;
    left: 54px;
    top: 944px;
    width: 796px;
    margin: 0;
    font-family: "PT Sans", sans-serif;
    font-size: 25px;
    line-height: 34px;
    color: var(--ink);
    text-align: justify;
  }
</style>
</head>
<body>
<main class="flyer">
  <svg class="backdrop" width="885" height="1200" viewBox="0 0 885 1200" aria-hidden="true">
    <defs>
      <linearGradient id="edge-shade" x1="0" y1="0" x2="1" y2="0">
        <stop offset="0" stop-color="#555" stop-opacity="0.9"/>
        <stop offset="1" stop-color="#777" stop-opacity="0.6"/>
      </linearGradient>
    </defs>
    <polygon class="band-sky" points="290,0 735,0 420,375 0,490 0,248" fill="var(--sky)"/>
    <polygon class="band-rose-side" points="735,0 752,0 425,376 405,372" fill="#c9c9cb"/>
    <polygon class="band-rose" points="752,0 885,0 885,484 425,376" fill="var(--rose)"/>
    <polygon class="band-rose-foot" points="425,376 885,484 885,500 440,388" fill="#bdbdbf"/>
    <polygon class="band-sun" points="117,350 885,508 885,1176 0,1176 0,490" fill="var(--sun)"/>
    <polygon class="band-sun-edge" points="117,343 885,500 885,510 117,352" fill="url(#edge-shade)"/>
    <rect class="logo-underline" x="0" y="278" width="480" height="5" fill="url(#edge-shade)"/>
    <rect class="foot-rose" x="0" y="1176" width="443" height="24" fill="var(--rose)"/>
    <rect class="foot-sky" x="443" y="1176" width="442" height="24" fill="var(--sky)"/>
  </svg>

  <header class="brand-plate">
    <span class="brand-dot"></span>
    <span class="brand-name">Bright Lane<br>Tutors</span>
  </header>

  <section class="offer">
    <p class="offer-title">INTRODUCTORY<br>OFFER</p>
    <p class="offer-detail">of 20% off all courses</p>
  </section>

  <ul class="checklist">
    <li class="item-subject">Chosen Subject/<span class="zh">选中的科目</span></li>
    <li class="item-timetable">Received Timetable/<span class="zh">收到的时间表</span></li>
    <li class="item-speaking">Confident in Public Speaking/</li>
    <li class="item-speaking-zh"><span class="zh">在公开场合自信演讲</span></li>
    <li class="item-fridge">Fridge full of Volt Fizz /<span class="zh">满冰箱的伏特</span></li>
    <li class="item-best">Prepared to be my very best/<span class="zh">做最好的自己</span></li>
  </ul>

  <p class="web-link">Visited brightlanetutors.com.au</p>
  <p class="about">Bright Lane Tutors exists to help university students with real life skill development such as public speaking. We aim to equip students with skills that are not taught in the university environment to enable them to maximise their results.</p>
</main>
</body>
</html>
```